KT Holdings Company brochure

require the design of a brochure for my company KT holdings which incorporates 2 separate companies specialising in home technology and security. Im not sure whether its going to be best to do one brochure with all the info in or 2 individual ones

Target Market(s)

Footballers and High net worth individuals

Industry/Entity Type

Information Technology

Font styles to use
Serif
Other font styles liked:
• Neuropol (this is the logo font)

Colors
ec1f27
000000
9d9d9d

Requirements
Must have
• 2 sections one for audio visual and 1 for security

```html
<!DOCTYPE html>
<html lang="en">
<head>
<meta charset="utf-8">
<title>KT Holdings – Company Brochure</title>
<link href="https://fonts.googleapis.com/css2?family=Open+Sans:ital,wght@0,400;0,600;1,400;1,600&display=swap" rel="stylesheet">
<style>
  :root{
    --red:#ec1f27;
    --black:#000000;
    --grey:#9d9d9d;
    --paper:#f3f3f4;
    --white:#ffffff;
    --ink:#333333;
  }
  *{margin:0;padding:0;box-sizing:border-box}
  html,body{width:800px;height:1200px;overflow:hidden;background:#e6e6e6;font-family:"Open Sans",Arial,sans-serif}
  .spread{position:absolute;left:20px;width:760px;box-shadow:0 4px 14px rgba(0,0,0,.25);overflow:hidden}
  .spread--outer{top:20px;height:530px}
  .spread--inner{top:600px;height:580px;background:var(--paper)}
  .spread svg{position:absolute;left:0;top:0}
  .about{position:absolute;left:158px;top:36px;width:140px;color:var(--white);font-size:9px;line-height:1.45}
  .about h2{font-size:11px;font-weight:400;margin-bottom:6px}
  .contact{position:absolute;color:var(--white);font-size:10px;line-height:1.35}
  .contact--address{left:34px;top:448px}
  .contact--phone{left:180px;top:468px}
  .contact--email{left:250px;top:428px}
  .contact--web{left:470px;top:436px}
  .contact--address::before,.contact--phone::before,.contact--email::before,.contact--web::before{
    content:"";display:inline-block;width:6px;height:6px;border-radius:50%;background:var(--red);margin-right:6px;vertical-align:middle}
  .brand{position:absolute;left:610px;top:360px;display:flex;align-items:center;gap:8px;color:var(--red);font-size:17px;font-weight:600}
  .brand-dot{width:26px;height:26px;border-radius:50%;background:var(--red)}
  .page{position:absolute;top:26px;width:340px;font-size:8px;line-height:1.4;color:var(--ink)}
  .page--left{left:30px}
  .page--right{left:405px;top:90px}
  .service{margin-bottom:7px}
  .service h3{color:var(--red);font-size:11px;font-weight:600;margin-bottom:2px}
  .service li{list-style:none;padding-left:11px;position:relative}
  .service li::before{content:"✓";position:absolute;left:0;color:var(--red);font-weight:600}
  .web-inner{position:absolute;left:560px;top:548px;color:var(--white);font-size:10px}
  .web-inner::before{content:"";display:inline-block;width:6px;height:6px;border-radius:50%;background:var(--red);margin-right:6px;vertical-align:middle}
</style>
</head>
<body>

<section class="spread spread--outer">
  <svg width="760" height="530" viewBox="0 0 760 530">
    <defs>
      <linearGradient id="diningTone" x1="0" y1="0" x2="1" y2="1">
        <stop offset="0" stop-color="#efe7dc"/>
        <stop offset=".5" stop-color="#b9a6a0"/>
        <stop offset="1" stop-color="#3e2e45"/>
      </linearGradient>
      <linearGradient id="poolTone" x1="0" y1="0" x2="0" y2="1">
        <stop offset="0" stop-color="#1e3fc4"/>
        <stop offset=".22" stop-color="#2f58d6"/>
        <stop offset=".36" stop-color="#ece4d6"/>
        <stop offset=".55" stop-color="#b07a4a"/>
        <stop offset=".72" stop-color="#6f6a62"/>
        <stop offset=".88" stop-color="#9fdcdc"/>
      </linearGradient>
    </defs>
    <rect class="photo-dining" x="0" y="0" width="380" height="460" fill="url(#diningTone)" role="img" aria-label="Photo of a luxury dining room with chandelier and purple chairs"/>
    <rect class="photo-pool" x="380" y="0" width="380" height="420" fill="url(#poolTone)" role="img" aria-label="Photo of a modern villa terrace with pool at dusk"/>
    <rect class="about-panel" x="145" y="0" width="160" height="460" fill="#ec1f27" opacity=".88"/>
    <rect class="partner-badge" x="178" y="308" width="96" height="76" rx="6" fill="#ffffff"/>
    <rect x="186" y="316" width="80" height="60" rx="4" fill="#ec1f27"/>
    <path d="M0,404 C200,408 480,352 760,286" fill="none" stroke="#d6d6d6" stroke-width="6"/>
    <path d="M0,410 C200,414 480,358 760,292" fill="none" stroke="#ec1f27" stroke-width="5"/>
    <path d="M0,416 C200,420 480,364 760,298 L760,530 L0,530 Z" fill="#000000"/>
    <line x1="380" y1="0" x2="380" y2="530" stroke="rgba(0,0,0,.15)"/>
  </svg>

  <div class="about">
    <h2>About us</h2>
    <p>With offices in London and Newcastle, we design, install and service entertainment and control systems for our clients. The service is personal, unintimidating and of the highest quality. We create systems that enrich and support our clients' lives, giving them the technology they need without the compromise.</p>
  </div>

  <p class="contact contact--address">Kestrel Tech Ltd<br>Alder House<br>118-120 Riverside Way<br>London<br>SE9 4QT</p>
  <p class="contact contact--phone">0207 555 0142</p>
  <p class="contact contact--email">info@kestreltech.co.uk</p>
  <p class="contact contact--web">www.kestreltech.co.uk</p>

  <div class="brand"><span class="brand-dot"></span>KT Holdings</div>
</section>

<section class="spread spread--inner">
  <svg width="760" height="580" viewBox="0 0 760 580">
    <line x1="380" y1="0" x2="380" y2="450" stroke="#dcdcdc"/>
    <path d="M0,445 C180,475 380,525 560,525 C650,525 710,515 760,505 L760,580 L0,580 Z" fill="#000000"/>
    <path d="M0,455 C150,475 260,515 380,510 C520,503 620,478 760,482" fill="none" stroke="#ec1f27" stroke-width="6"/>
    <g class="thumbs" stroke="#ec1f27" stroke-width="3">
      <circle cx="58" cy="456" r="30" fill="#c49a5a" role="img" aria-label="Photo of a lit lounge interior"/>
      <circle cx="130" cy="488" r="22" fill="#8c8c94" role="img" aria-label="Photo of a media room"/>
      <circle cx="186" cy="503" r="18" fill="#b8a690" role="img" aria-label="Photo of a hallway interior"/>
      <circle cx="440" cy="508" r="20" fill="#a7a2a0" role="img" aria-label="Photo of a kitchen"/>
      <circle cx="520" cy="498" r="26" fill="#d2d4d8" role="img" aria-label="Photo of a white living room"/>
      <circle cx="612" cy="490" r="32" fill="#5a3fc8" role="img" aria-label="Photo of a cinema room with purple lighting"/>
    </g>
  </svg>

  <div class="page page--left">
    <div class="service"><h3>Audio Visual Systems</h3><ul>
      <li>Easy, discreet access to all your music, wherever you are in your home or garden</li>
      <li>Tunely, Streamora, Internet Radio, DAB etc all supported</li>
      <li>Full HD TV and direct access to your personal TV recordings wherever you are in the house</li>
      <li>We're committed to the highest quality music and images – even old school Hi-Fi buffs can get what they need from our team</li></ul></div>
    <div class="service"><h3>Home Cinema</h3><ul>
      <li>Professionally designed home cinema – tailored to suit your budget and your space</li>
      <li>We can deliver dedicated projection screening rooms with sound and images equalling commercial cinemas or discreet solutions that disappear when they're not needed</li>
      <li>Who will love this more – you or your kids?</li></ul></div>
    <div class="service"><h3>Lighting Control and Design</h3><ul>
      <li>Mood lighting – whole room or house control from a single button press</li>
      <li>Energy efficient lighting</li>
      <li>Automated window treatments from world leading manufacturer Lumara</li>
      <li>Full automation giving control and timer functions when you are away from home</li></ul></div>
    <div class="service"><h3>Access Control</h3><ul>
      <li>Video and audio door entry to keep your property secure</li>
      <li>Control from your tablet, smartphone, dedicated wireless handsets and wall units</li>
      <li>"Frictionless" access for trusted individuals or vehicles via RFID, biometrics and PIN codes</li>
      <li>Automation of gates and barriers</li></ul></div>
    <div class="service"><h3>Tender Design Consultants</h3><ul>
      <li>Work closely with client to establish brief for tender</li>
      <li>Work with design team to define a bespoke package</li>
      <li>Fully documented to allow for easy cost comparison between installation companies</li>
      <li>Review submitted tenders for compliance to brief</li></ul></div>
  </div>

  <div class="page page--right">
    <div class="service"><h3>Communications/ Broadband Networks</h3><ul>
      <li>Data networking – a solid infrastructure for now and the future</li>
      <li>"Designed in" robustness and security</li>
      <li>Reliable WiFi network in all areas of the house including garden (if required)</li>
      <li>Analogue, Digital and SIP "cloud" based phone systems</li>
      <li>In house expertise on file sharing, secure backups, equipment synchronising and "cloud" based solutions</li>
      <li>Supply of dedicated Fiber optic leased line connections upto 1GB guaranteed</li>
      <li>Mobile phone signal boosting</li></ul></div>
    <div class="service"><h3>CCTV/ Security</h3><ul>
      <li>Personal reassurance while you are at home and confidence when you are away</li>
      <li>Access images remotely on all your devices, where ever you are in the world</li>
      <li>High definition IP cameras giving evidence grade recordings</li>
      <li>Alarms installed and certified upto grade 1 response category with two way audio</li></ul></div>
    <div class="service"><h3>Climate Control/ Renewable Energy</h3><ul>
      <li>Combining internal and external sensors provides "intelligent" control that reduces energy consumption</li>
      <li>View and manage energy usage on your control interface</li>
      <li>Integrate and manage micro generation information</li>
      <li>Solar power, wind turbines and hydro generation can all be accommodated</li></ul></div>
    <div class="service"><h3>Bespoke Solutions</h3><ul>
      <li>Single unified control platform for multiple systems from different manufacturers</li>
      <li>Personalised control including 3D floorplans and client specific graphics</li>
      <li>Control water features, alerts from security/fire alarms</li>
      <li>Automation of doors, windows and blinds</li>
      <li>Automation of TV Brackets and Pop Mechanisms (link to Home Automation Page)</li></ul></div>
  </div>

  <p class="web-inner">www.kestreltech.co.uk</p>
</section>

</body>
</html>
```